Real Estate Acquisition Company Needs Business Card Design

Tellwyn Real Estate is in need of a business card design!

As a Real Estate Acquisition Company, Tellwyn Real Estate conducts mutually beneficial real estate transactions that actively consider the needs of the seller. At Tellwyn Real Estate we’re actively buying properties from those that see value in a direct transaction, but more importantly want reassurances that they, personally, are in integral part of it. Of course, it all starts with fair market value, but it doesn’t stop there. We’ve found the most success when we offer more. And with our deep experience in this industry, we’ve discovered that we have a lot to offer!

We already have a logo and brand guidelines that we've uploaded. Our final design should stay true to the guidelines. We are looking for a business card design that has two names (Ex. Jane Doe & John Doe) and contact information for each person- this way the company principals can share a card as they often do business as a team.
Updates

The criteria was unfortunately not met on most designs. We are looking for a card that has a layout for TWO names and respective contact information for each of the two people. Almost all designs only had a space for one name and one set of contact information.

Industry/Entity Type

Real Estate

Contact Information for Business Card

We are looking for a business card design that has two names (Ex. Jane Doe & John Doe) and each of their contact information- this way the company principals can share a card as they often do business as a team.

Font styles to use
Other font styles liked:
• Use Brand Guidelines

Requirements
Must have
• Please stay true to our Brand Guidelines for colours, fonts, and positioning of logo.

We require a layout for two names and respective contact information. The company principals work as a team and want a card that has both their information on it.

```html
<!DOCTYPE html>
<html lang="en">
<head>
<meta charset="utf-8">
<title>Tellwyn Real Estate – Business Card</title>
<link href="https://fonts.googleapis.com/css2?family=Fira+Sans:ital,wght@0,300;0,400;0,500;1,600&display=swap" rel="stylesheet">
<style>
  :root {
    --backdrop: #1d1d1d;
    --navy: #14213a;
    --gold: #f2a92c;
    --white: #ffffff;
    --ink: #1b2742;
    --grey-text: #4a4f5a;
    --divider: #b9bcc2;
  }
  * { box-sizing: border-box; margin: 0; padding: 0; }
  html, body {
    width: 1200px; height: 1200px; overflow: hidden;
    background: var(--backdrop);
    font-family: "Fira Sans", sans-serif;
  }
  .sheet {
    width: 1200px; height: 1200px;
    display: flex; flex-direction: column;
    align-items: center; justify-content: center; gap: 60px;
  }
  .card {
    width: 880px; height: 503px;
    position: relative;
    border-radius: 4px;
    box-shadow: 0 18px 40px rgba(0,0,0,.5);
  }
  /* Front */
  .card--front {
    background: var(--navy);
    display: flex; align-items: center; justify-content: center;
  }
  .brand { text-align: right; color: var(--white); }
  .brand__name {
    display: block;
    font-weight: 300; font-size: 96px; letter-spacing: 2px; line-height: 1;
  }
  .brand__sub {
    display: block; margin-top: 10px;
    font-weight: 300; font-size: 22px; letter-spacing: 6px;
  }
  /* Back */
  .card--back { background: var(--white); color: var(--ink); }
  .people {
    position: absolute; top: 92px; left: 0; right: 0;
    display: flex; justify-content: center;
  }
  .person { width: 290px; padding: 0 30px; }
  .person--left { text-align: right; border-right: 1.5px solid var(--divider); }
  .person__name { font-weight: 500; font-size: 34px; line-height: 1.1; }
  .person__role { color: var(--gold); font-size: 19px; margin: 4px 0 14px; }
  .contact {
    display: flex; align-items: center; gap: 10px;
    font-size: 18px; color: var(--grey-text); line-height: 1.55;
  }
  .person--left .contact { justify-content: flex-end; }
  .icon { width: 16px; height: 16px; flex: none; }
  .rule {
    position: absolute; left: 120px; right: 120px; top: 306px;
    height: 1px; background: var(--gold);
  }
  .company {
    position: absolute; top: 330px; left: 0; right: 0;
    text-align: center; color: var(--grey-text); font-size: 18px; line-height: 1.6;
  }
  .company__name { color: var(--ink); font-style: italic; font-weight: 600; font-size: 20px; }
</style>
</head>
<body>
<main class="sheet">
  <section class="card card--front">
    <div class="brand">
      <span class="brand__name">TELLWYN</span>
      <span class="brand__sub">REAL ESTATE INC.</span>
    </div>
  </section>

  <section class="card card--back">
    <div class="people">
      <div class="person person--left">
        <p class="person__name">John Doe</p>
        <p class="person__role">Director</p>
        <p class="contact">000.123.1234
          <svg class="icon" viewBox="0 0 16 16"><circle cx="8" cy="8" r="8" fill="#f2a92c"/><path d="M5 4.5l1.6-.4 1 2-1 .8a5 5 0 0 0 2.5 2.5l.8-1 2 1-.4 1.6C9 11.5 4.5 7 5 4.5z" fill="#fff"/></svg>
        </p>
        <p class="contact">john@tellwyn.com
          <svg class="icon" viewBox="0 0 16 16"><circle cx="8" cy="8" r="8" fill="#f2a92c"/><rect x="4" y="5.2" width="8" height="5.6" rx="0.8" fill="#fff"/><path d="M4.3 5.6L8 8.4l3.7-2.8" stroke="#f2a92c" stroke-width="0.9" fill="none"/></svg>
        </p>
      </div>
      <div class="person person--right">
        <p class="person__name">Jane Doe</p>
        <p class="person__role">Director</p>
        <p class="contact">
          <svg class="icon" viewBox="0 0 16 16"><circle cx="8" cy="8" r="8" fill="#f2a92c"/><path d="M5 4.5l1.6-.4 1 2-1 .8a5 5 0 0 0 2.5 2.5l.8-1 2 1-.4 1.6C9 11.5 4.5 7 5 4.5z" fill="#fff"/></svg>
          000.123.1234</p>
        <p class="contact">
          <svg class="icon" viewBox="0 0 16 16"><circle cx="8" cy="8" r="8" fill="#f2a92c"/><rect x="4" y="5.2" width="8" height="5.6" rx="0.8" fill="#fff"/><path d="M4.3 5.6L8 8.4l3.7-2.8" stroke="#f2a92c" stroke-width="0.9" fill="none"/></svg>
          jane@tellwyn.com</p>
      </div>
    </div>
    <div class="rule"></div>
    <div class="company">
      <p class="company__name">Tellwyn Real Estate INC.</p>
      <p>www.tellwyn.com</p>
      <p>Dummy city, Dummy country, land</p>
    </div>
  </section>
</main>
</body>
</html>
```